standardize print collateral

we need help standardizing all print collateral and website. top priorities:

1. standardized case studies template
2. standardized marketing slicks template
3. standardized powerpoint template
Updates

Project Deadline Extended
Reason: We are extending the project to allow current design submissions to be tweaked while providing the opportunity for new designs to be submitted. We will need all 3 collateral designs submitted to make a final decision. Please note, these 3 designs should all look different, needless to say they should all compliment eachother. As for some direction, the powerpoint main color should not be yellow since yellow does not show up the same shade on any screen. The case study and marketing slicks will be printed and often sit next to our competitors marketing material - think high end product, technology, revolutionary, edgy, professional. The designs should compliment eachother and feel like the Brightfen Metrics brand (which you are determining) and should stand out professionally. We are open to introducing new colors into our brand, the only thing that must remain the same is our logo. Have fun, make it edgy, and keep it professional. Looking forward to seeing what you submit!

Target Market(s)

Property Casualty Insurance Companies: Executive level wording with actuarial credibility

Industry/Entity Type

Marketing

Requirements
Must have
• professional layout for existing collateral and 2-page marketing slicks. style guide/colors can be transferred to powerpoint. logo must stay; everything else (i.e. color, font, layout/structure etc.) is flexible. The three components should not looks the same, they should only compliment eachother.
Nice to have
• we are revolutionizing a conservative industry, so adequate level of edgy/advanced technology/impactful feel to layout
Should not have
• no need to stay within color constraints of yellow, but need to appropriately work well with the eagle head logo

```html
<!DOCTYPE html>
<html lang="en">
<head>
<meta charset="utf-8">
<title>Brightfen Metrics – Vantor Overview</title>
<link rel="stylesheet" href="https://fonts.googleapis.com/css2?family=Oswald:wght@300;400;600&family=Roboto+Condensed:wght@400;700&family=Arimo:wght@400;700&display=swap">
<style>
  :root{
    --teal:#0d7d74;
    --teal-dark:#0a6b63;
    --gold:#d6a82a;
    --ink:#262626;
    --bar:#4a76ad;
    --grid:#c9c9c9;
    --paper:#ffffff;
  }
  *{box-sizing:border-box;margin:0;padding:0}
  html,body{width:927px;height:1200px;overflow:hidden;background:var(--paper)}
  body{position:relative;font-family:"Roboto Condensed",Arial,sans-serif;color:var(--ink)}
  .band{position:absolute;left:0;width:927px;background:var(--teal);color:#fff;
        display:flex;align-items:center;justify-content:center;text-align:center;
        font-size:16px;line-height:1.45}
  .band--intro{top:26px;height:76px}
  .band--report{top:533px;height:74px}
  .section-title{position:absolute;font-family:"Oswald",sans-serif;font-weight:300;
        font-size:22px;color:var(--teal);letter-spacing:.5px;text-align:center;text-transform:uppercase}
  .section-title b{font-weight:600}
  .section-lede{position:absolute;text-align:center;font-size:15.5px;line-height:1.4}
  .chart-frame{position:absolute;border:3px solid var(--gold);background:#fff}
  .chart-frame::before{content:"";position:absolute;top:-11px;right:-11px;width:30px;height:30px;
        border-top:5px solid var(--teal);border-right:5px solid var(--teal)}
  .chart-frame::after{content:"";position:absolute;bottom:-11px;left:-11px;width:30px;height:30px;
        border-bottom:5px solid var(--teal);border-left:5px solid var(--teal)}
  .chart-frame svg{display:block;width:100%;height:100%;font-family:"Arimo",Arial,sans-serif}
  .tick{font-size:9px;fill:#333}
  .axis-title{font-size:9.5px;font-weight:700;fill:#333}
  .closing{position:absolute;top:996px;left:60px;width:807px;text-align:center;font-size:15.5px;line-height:1.45}
  .footer{position:absolute;left:0;top:1068px;width:927px;height:132px;background:var(--teal)}
  .brand{position:absolute;left:30px;top:70px;display:flex;align-items:center;gap:10px;
        font-family:"Roboto Condensed",sans-serif;font-weight:700;font-size:21px;color:#fff}
  .brand-dot{width:18px;height:18px;border-radius:50%;background:var(--gold)}
  .contact{position:absolute;left:640px;top:40px;color:#fff;font-size:15px;line-height:1.45;font-weight:700}
</style>
</head>
<body>

<header class="band band--intro">
  <p>Vantor detects, measures and presents actionable options to correct the effects of<br>adverse selection within any P&amp;C portfolio.</p>
</header>

<h2 class="section-title" style="left:27px;top:140px;width:397px">Underwriting <b>Score</b></h2>
<p class="section-lede" style="left:20px;top:187px;width:411px">Discover the pricing imbalances within the portfolio.<br>These imbalances are the main driver of the adverse selection.</p>

<h2 class="section-title" style="left:482px;top:140px;width:412px"><b>Trend</b> and <b>Loss</b> Ratio</h2>
<p class="section-lede" style="left:470px;top:187px;width:436px">Show trends within the portfolio in real time covering premium<br>adequacy and the quality of all business being written.</p>

<!-- Loss ratio by score tier -->
<figure class="chart-frame" style="left:27px;top:265px;width:397px;height:227px">
  <svg viewBox="0 0 391 221" role="img" aria-label="Bar chart of loss ratio by score tier">
    <g class="tick" text-anchor="end">
      <text x="56" y="193">0%</text><text x="56" y="171">10%</text><text x="56" y="149">20%</text>
      <text x="56" y="127">30%</text><text x="56" y="105">40%</text><text x="56" y="83">50%</text>
      <text x="56" y="61">60%</text><text x="56" y="39">70%</text><text x="56" y="17">80%</text>
    </g>
    <line x1="60" y1="14" x2="60" y2="190" stroke="#888"/>
    <line x1="60" y1="190" x2="385" y2="190" stroke="#888"/>
    <g fill="var(--bar)">
      <rect x="73" y="41" width="28" height="149"/>
      <rect x="127" y="85" width="28" height="105"/>
      <rect x="181" y="122" width="28" height="68"/>
      <rect x="235" y="129" width="28" height="61"/>
      <rect x="289" y="146" width="28" height="44"/>
      <rect x="343" y="151" width="28" height="39"/>
    </g>
    <g class="tick" text-anchor="middle">
      <text x="87" y="202">0-98</text><text x="141" y="202">99- 249</text><text x="195" y="202">250-499</text>
      <text x="249" y="202">500- 749</text><text x="303" y="202">750- 899</text><text x="357" y="202">900 - 1000</text>
    </g>
    <text class="axis-title" x="222" y="214" text-anchor="middle">Score Tier</text>
    <text class="axis-title" transform="translate(18 102) rotate(-90)" text-anchor="middle">Loss Ratio</text>
  </svg>
</figure>

<!-- Loss ratio versus growth -->
<figure class="chart-frame" style="left:482px;top:265px;width:412px;height:227px">
  <svg viewBox="0 0 406 221" role="img" aria-label="Bubble chart of loss ratio against growth for four segments">
    <defs>
      <radialGradient id="bubble" cx="45%" cy="40%" r="60%">
        <stop offset="0" stop-color="#ffffff"/><stop offset="1" stop-color="#b9c9dc"/>
      </radialGradient>
    </defs>
    <g class="tick" text-anchor="end">
      <text x="38" y="193">0%</text><text x="38" y="164">10%</text><text x="38" y="135">20%</text>
      <text x="38" y="106">30%</text><text x="38" y="77">40%</text><text x="38" y="48">50%</text><text x="38" y="19">60%</text>
    </g>
    <line x1="42" y1="190" x2="395" y2="190" stroke="#888"/>
    <line x1="183" y1="14" x2="183" y2="190" stroke="#888"/>
    <line x1="42" y1="73" x2="372" y2="73" stroke="var(--bar)" stroke-width="2.5"/>
    <text class="tick" x="376" y="76">40%</text>
    <g stroke="#aebfd4" fill="url(#bubble)">
      <circle cx="370" cy="41" r="21"/>
      <circle cx="147" cy="127" r="21"/>
      <circle cx="195" cy="91" r="21"/>
      <circle cx="213" cy="65" r="21"/>
    </g>
    <g font-size="11" font-weight="700" fill="#444" text-anchor="middle">
      <text x="370" y="45">1</text><text x="147" y="131">2</text><text x="195" y="95">4</text><text x="213" y="69">3</text>
    </g>
    <g class="tick" text-anchor="middle">
      <text x="42" y="202">-40%</text><text x="112" y="202">-20%</text><text x="183" y="202">0%</text>
      <text x="254" y="202">20%</text><text x="325" y="202">40%</text><text x="395" y="202">60%</text>
    </g>
    <text class="axis-title" x="218" y="214" text-anchor="middle">Growth/Decline</text>
    <text class="axis-title" transform="translate(10 102) rotate(-90)" text-anchor="middle">Loss Ratio</text>
  </svg>
</figure>

<section class="band band--report">
  <p>Report on detailed analyses including sales trend and profitability trends. This allows for a<br>method of managing distribution channels while addressing pricing imbalances.</p>
</section>

<h2 class="section-title" style="left:27px;top:634px;width:397px">Portfolio <b>Exposure</b></h2>
<h2 class="section-title" style="left:482px;top:634px;width:412px"><b>Premium</b> Change</h2>

<!-- Portfolio score over time -->
<figure class="chart-frame" style="left:27px;top:674px;width:397px;height:212px">
  <svg viewBox="0 0 391 206" role="img" aria-label="Line chart of portfolio score by quarter">
    <g stroke="var(--grid)" stroke-width=".6">
      <line x1="50" y1="12" x2="385" y2="12"/><line x1="50" y1="28" x2="385" y2="28"/>
      <line x1="50" y1="45" x2="385" y2="45"/><line x1="50" y1="61" x2="385" y2="61"/>
      <line x1="50" y1="78" x2="385" y2="78"/><line x1="50" y1="94" x2="385" y2="94"/>
      <line x1="50" y1="111" x2="385" y2="111"/><line x1="50" y1="127" x2="385" y2="127"/>
      <line x1="50" y1="144" x2="385" y2="144"/>
    </g>
    <line x1="50" y1="12" x2="50" y2="160" stroke="#888"/>
    <line x1="50" y1="160" x2="385" y2="160" stroke="#888"/>
    <g class="tick" text-anchor="end">
      <text x="46" y="15">550</text><text x="46" y="31">540</text><text x="46" y="48">530</text>
      <text x="46" y="64">520</text><text x="46" y="81">510</text><text x="46" y="97">500</text>
      <text x="46" y="114">490</text><text x="46" y="130">480</text><text x="46" y="147">470</text><text x="46" y="163">460</text>
    </g>
    <polyline fill="none" stroke="var(--bar)" stroke-width="2"
      points="55,56 65,43 76,45 86,53 97,50 107,28 118,31 128,41 139,41 149,25 160,28 170,45 181,41 191,28 202,31 212,41 223,54 233,38 244,36 254,48 265,56 275,51 286,59 296,84 307,96 317,86 328,87 338,100 349,102 359,87 370,92 380,102"/>
    <g class="tick" font-size="8">
      <text transform="translate(58 200) rotate(-90)">2001/Q1</text>
      <text transform="translate(84 200) rotate(-90)">2001/Q3</text>
      <text transform="translate(110 200) rotate(-90)">2002/Q1</text>
      <text transform="translate(136 200) rotate(-90)">2002/Q3</text>
      <text transform="translate(162 200) rotate(-90)">2003/Q1</text>
      <text transform="translate(188 200) rotate(-90)">2003/Q3</text>
      <text transform="translate(214 200) rotate(-90)">2004/Q1</text>
      <text transform="translate(240 200) rotate(-90)">2004/Q3</text>
      <text transform="translate(266 200) rotate(-90)">2005/Q1</text>
      <text transform="translate(292 200) rotate(-90)">2005/Q3</text>
      <text transform="translate(318 200) rotate(-90)">2006/Q1</text>
      <text transform="translate(344 200) rotate(-90)">2006/Q3</text>
      <text transform="translate(370 200) rotate(-90)">2007/Q1</text>
    </g>
    <text class="axis-title" transform="translate(12 86) rotate(-90)" text-anchor="middle">Portfolio Score</text>
  </svg>
</figure>

<!-- Premium change by segment -->
<figure class="chart-frame" style="left:482px;top:674px;width:412px;height:212px">
  <svg viewBox="0 0 406 206" role="img" aria-label="Bar chart of premium change by segment">
    <g stroke="var(--grid)" stroke-width=".6">
      <line x1="55" y1="12" x2="395" y2="12"/><line x1="55" y1="35" x2="395" y2="35"/>
      <line x1="55" y1="57" x2="395" y2="57"/><line x1="55" y1="102" x2="395" y2="102"/>
      <line x1="55" y1="125" x2="395" y2="125"/><line x1="55" y1="147" x2="395" y2="147"/>
      <line x1="55" y1="170" x2="395" y2="170"/>
    </g>
    <line x1="55" y1="12" x2="55" y2="170" stroke="#888"/>
    <line x1="55" y1="80" x2="395" y2="80" stroke="#888"/>
    <g class="tick" text-anchor="end">
      <text x="50" y="15">60%</text><text x="50" y="38">40%</text><text x="50" y="60">20%</text>
      <text x="50" y="83">0%</text><text x="50" y="105">-20%</text><text x="50" y="128">-40%</text>
      <text x="50" y="150">-60%</text><text x="50" y="173">-80%</text>
    </g>
    <g fill="var(--bar)">
      <rect x="84" y="80" width="26" height="7"/>
      <rect x="169" y="80" width="26" height="68"/>
      <rect x="254" y="26" width="26" height="54"/>
      <rect x="339" y="52" width="26" height="28"/>
    </g>
    <g class="tick" text-anchor="middle">
      <text x="97" y="94">1</text><text x="182" y="94">2</text><text x="267" y="94">3</text><text x="352" y="94">4</text>
    </g>
    <text class="axis-title" x="225" y="188" text-anchor="middle">Segment Number</text>
    <text class="axis-title" transform="translate(14 92) rotate(-90)" text-anchor="middle">% Change</text>
  </svg>
</figure>

<p class="closing">Brightfen Metrics provides breakthrough predictive analytics powered by machine learning and the latest statistical techniques, enabling property and casualty insurers to achieve superior performance.</p>

<footer class="footer">
  <div class="brand"><span class="brand-dot"></span>Brightfen Metrics</div>
  <address class="contact" style="font-style:normal">
    214 Larkspur Avenue, Suite 410 Greenvale, SC 29460<br>
    Phone: 803-555-0142 | Fax: 803-555-0187<br>
    www.brightfenmetrics.com
  </address>
</footer>

</body>
</html>
```